New Business Card Design Project

I need a meaningful new business card. Therefore, the website should convey growth, joy, uniqueness, workout and a bit of luxury.
Color scheme should be petrol, gold and matching colors.

```html
<!DOCTYPE html>
<html lang="en">
<head>
<meta charset="utf-8">
<title>Corewell Studio – Business Card</title>
<link rel="stylesheet" href="https://fonts.googleapis.com/css2?family=Cinzel:wght@400;600&family=Pinyon+Script&display=swap">
<style>
  :root {
    --page: #ffffff;
    --card-dark: #000000;
    --card-light: #f9f7f0;
    --gold: #c9a13b;
    --gold-light: #f3d77a;
    --gold-mid: #e9c46a;
    --gold-deep: #d9a85a;
    --ink: #111111;
    --ornament: #cfc8b6;
    --guide: #b5b5b5;
  }
  html, body {
    margin: 0;
    padding: 0;
    width: 1200px;
    height: 1200px;
    overflow: hidden;
    background: var(--page);
  }
  .canvas {
    position: relative;
    width: 1200px;
    height: 1200px;
  }
  .card {
    position: absolute;
    left: 286px;
    width: 628px;
    height: 358px;
    border-radius: 10px;
    overflow: hidden;
  }
  .card--front {
    top: 192px;
    background: var(--card-dark);
  }
  .card--back {
    top: 598px;
    background: var(--card-light);
  }
  .brand {
    position: absolute;
    font-family: "Cinzel", serif;
    font-weight: 600;
    text-align: center;
    letter-spacing: 2px;
    line-height: 1.15;
    margin: 0;
  }
  .brand__mark {
    display: inline-block;
    width: 14px;
    height: 14px;
    border-radius: 50%;
    margin-bottom: 10px;
  }
  .card--front .brand {
    left: 0;
    right: 0;
    top: 132px;
    font-size: 40px;
    color: var(--gold);
  }
  .card--front .brand__mark { background: var(--gold); }
  .card--back .brand {
    left: 24px;
    width: 212px;
    top: 108px;
    font-size: 30px;
    color: var(--ink);
  }
  .card--back .brand__mark { background: var(--ink); width: 11px; height: 11px; }
  .divider {
    position: absolute;
    left: 257px;
    top: 28px;
    width: 2px;
    height: 252px;
    background: var(--ink);
  }
  .holder {
    position: absolute;
    left: 286px;
    width: 320px;
    top: 78px;
    text-align: center;
  }
  .holder__name {
    font-family: "Pinyon Script", cursive;
    font-size: 44px;
    color: var(--ink);
    margin: 0;
    line-height: 60px;
  }
  .holder__ornament {
    position: absolute;
    top: 14px;
    width: 34px;
    height: 30px;
    border-radius: 15px;
    background: var(--ornament);
  }
  .holder__ornament--left { left: -4px; }
  .holder__ornament--right { right: -4px; }
  .holder__rule {
    width: 222px;
    height: 1px;
    background: var(--ink);
    margin: 2px auto 0;
  }
  .contact {
    position: absolute;
    left: 308px;
    top: 174px;
    margin: 0;
    font-family: "Cinzel", serif;
    font-size: 12px;
    color: var(--ink);
    line-height: 18px;
    letter-spacing: 0.4px;
  }
  .contact__row { display: flex; }
  .contact__label { width: 90px; }
  .wave {
    position: absolute;
    left: 0;
    top: 0;
    width: 628px;
    height: 358px;
  }
  .trim-guide {
    position: absolute;
    left: 346px;
    top: 956px;
    height: 52px;
    border-left: 1px dashed var(--guide);
  }
</style>
</head>
<body>
<div class="canvas">

  <section class="card card--front">
    <p class="brand"><span class="brand__mark"></span><br>Corewell<br>Studio</p>
  </section>

  <section class="card card--back">
    <svg class="wave" viewBox="0 0 628 358" aria-hidden="true">
      <defs>
        <linearGradient id="goldBand" x1="0" y1="0" x2="1" y2="0">
          <stop offset="0" stop-color="var(--gold-mid)"/>
          <stop offset="0.18" stop-color="var(--gold-light)"/>
          <stop offset="0.32" stop-color="var(--gold-deep)"/>
          <stop offset="0.5" stop-color="var(--gold-light)"/>
          <stop offset="0.62" stop-color="var(--gold-deep)"/>
          <stop offset="0.8" stop-color="var(--gold-mid)"/>
          <stop offset="1" stop-color="var(--gold-mid)"/>
        </linearGradient>
      </defs>
      <path d="M0 296 C40 280 110 270 200 285 C320 305 400 345 480 335 C560 325 600 280 628 248 L628 358 L0 358 Z" fill="url(#goldBand)"/>
    </svg>

    <p class="brand"><span class="brand__mark"></span><br>Corewell<br>Studio</p>

    <div class="divider"></div>

    <div class="holder">
      <span class="holder__ornament holder__ornament--left" role="img" aria-label="Leaf flourish ornament"></span>
      <p class="holder__name">Your Name</p>
      <span class="holder__ornament holder__ornament--right" role="img" aria-label="Leaf flourish ornament"></span>
      <div class="holder__rule"></div>
    </div>

    <div class="contact">
      <div class="contact__row">LINE ADDRES 123111111</div>
      <div class="contact__row"><span class="contact__label">PHONE</span><span>: 000000000000</span></div>
      <div class="contact__row"><span class="contact__label">MOBILE</span><span>: 0000 0000 0000</span></div>
      <div class="contact__row"><span class="contact__label">MAIL</span><span>: YOURMAIL@BOX.COM</span></div>
    </div>
  </section>

  <div class="trim-guide"></div>
</div>
</body>
</html>
```